QLDR Individual and Corporate Development Business Card Design

QLDR needs a business card design that is aligned with it's values and targetted markets. Harmonic Ladder of Reasoning Matrix's self diagnosis model and tools, which can be used for personal improvement and team/business performance enhancement, is based on the learnings of over 20 years of medical practitioning. QLDR supercharges personal effectiveness and awareness to also increase team and business performance.

The targetted markets are high performance individuals and teams who aspire seek to enhance their capabilities and achieve their absolute best potential.

Look and feel for the business card design we are looking for is high technology, premium, fresh, new and medical.

Target Market(s)

Industry/Entity Type

Business Consultant

Contact Information for Business Card

Logo, Full Name, Title, Phone number, Email, company name, Address,

Font styles to use
Sans Serif

Requirements
Must have
• Tag line: Maximising Performance for Highly Effective People
• Please use same colours as the logo.

```html
<!DOCTYPE html>
<html lang="en">
<head>
<meta charset="utf-8">
<title>QLDR Business Card</title>
<link rel="stylesheet" href="https://fonts.googleapis.com/css2?family=Open+Sans:wght@400;600;700&display=swap">
<style>
  :root{
    --teal:#0aa7c2;
    --ink:#050505;
    --paper:#ffffff;
    --grey:#7d8287;
    --soft-grey:#d4d7da;
    --stage:#3a3b3d;
  }
  *{margin:0;padding:0;box-sizing:border-box}
  html,body{width:1200px;height:880px;overflow:hidden}
  body{background:var(--stage);font-family:"Open Sans",Arial,sans-serif;position:relative}
  .card{position:absolute;width:620px;height:354px;overflow:hidden;box-shadow:0 10px 30px rgba(0,0,0,.45)}
  .card--front{left:70px;top:50px;background:var(--ink)}
  .card--back{left:510px;top:476px;background:var(--paper)}

  .wordmark{position:absolute;display:flex;flex-direction:column}
  .wordmark__name{color:var(--teal);font-weight:700;font-size:74px;line-height:1;letter-spacing:4px}
  .wordmark__rule{height:2px;background:var(--grey);margin:6px 0 5px}
  .wordmark__full{color:var(--teal);font-weight:600;font-size:15px;line-height:1.15;text-transform:uppercase;letter-spacing:.5px}
  .card--front .wordmark{left:200px;top:88px;width:240px}
  .card--back .wordmark{left:48px;top:108px;width:230px}
  .card--back .wordmark__name{font-size:66px}
  .card--back .wordmark__full{font-size:14px}

  .band{position:absolute;left:0;right:0;bottom:26px;height:44px;background:var(--teal);display:flex;align-items:center;justify-content:center;color:#fff}
  .band::after{content:"";position:absolute;left:0;right:0;top:48px;height:6px;background:var(--soft-grey)}
  .card--front .band::after{background:#2a2c2e}
  .band__text{font-size:17px;letter-spacing:1px}
  .card--back .band__text{font-weight:700;text-transform:uppercase;font-size:16px;letter-spacing:1.5px}

  .divider{position:absolute;left:318px;top:70px;width:1px;height:180px;background:var(--teal)}
  .contact{position:absolute;left:350px;top:74px;color:#333;font-size:14px;line-height:1.35}
  .contact__name{color:var(--teal);font-size:20px;text-transform:uppercase;line-height:1.1}
  .contact__title{margin-bottom:14px}
  .contact__address{margin-bottom:10px}
  .contact__line{display:flex;align-items:center;gap:7px}
  .contact__line svg{width:16px;height:16px;flex:none}
</style>
</head>
<body>
  <section class="card card--front" aria-label="Card front">
    <div class="wordmark">
      <span class="wordmark__name">QLDR</span>
      <span class="wordmark__rule"></span>
      <span class="wordmark__full">Harmonic Ladder of<br>Reasoning Matrix</span>
    </div>
    <div class="band"><span class="band__text">Maximising Performance for Highly Effective People</span></div>
  </section>

  <section class="card card--back" aria-label="Card back">
    <div class="wordmark">
      <span class="wordmark__name">QLDR</span>
      <span class="wordmark__rule"></span>
      <span class="wordmark__full">Harmonic Ladder of<br>Reasoning Matrix</span>
    </div>
    <div class="divider"></div>
    <div class="contact">
      <p class="contact__name">Mara Quinlan</p>
      <p class="contact__title">Founder</p>
      <p class="contact__address">PO BOX 418 Harbour Lane<br>7th street Brightwater</p>
      <p class="contact__line">
        <svg viewBox="0 0 16 16" aria-hidden="true"><circle cx="8" cy="8" r="7.2" fill="none" stroke="var(--teal)" stroke-width="1.2"/><rect x="5.5" y="3.8" width="5" height="8.4" rx="1" fill="none" stroke="var(--teal)" stroke-width="1.1"/></svg>
        (555) 014-2290
      </p>
      <p class="contact__line">
        <svg viewBox="0 0 16 16" aria-hidden="true"><circle cx="8" cy="8" r="7.2" fill="var(--teal)"/><rect x="4" y="5.2" width="8" height="5.6" fill="none" stroke="#fff" stroke-width="1"/><path d="M4 5.4 8 8.6 12 5.4" fill="none" stroke="#fff" stroke-width="1"/></svg>
        hello@qldrmail.com
      </p>
    </div>
    <div class="band"><span class="band__text">Harmonic Ladder of Reasoning Matrix</span></div>
  </section>
</body>
</html>
```